Startup Drone Platform Company business card

We are needing a business card design for our employees. We are a startup drone platform. We are looking for a business card that has our logo on one side, with the employee/company details on the opposite side. We are looking for something that is very eye catching, modern, and bold.

Target Market(s)

This will target both drone pilots and drone businesses, along with all the industries that could utilize drone services (aerial video, aerial photos, inspections, 3d mapping, etc).

Industry/Entity Type

Business

```html
<!DOCTYPE html>
<html lang="en">
<head>
<meta charset="utf-8">
<title>Skyhop Rentals – Business Card</title>
<link href="https://fonts.googleapis.com/css2?family=Roboto+Condensed:wght@300;400&display=swap" rel="stylesheet">
<style>
  :root {
    --backdrop: #6b6967;
    --card-black: #050505;
    --card-dark: #151515;
    --edge-cyan: #7fd6df;
    --ink-cyan: #8fdce4;
    --ink-muted: #2c3a3c;
  }
  * { margin: 0; padding: 0; box-sizing: border-box; }
  html, body {
    width: 1200px;
    height: 867px;
    overflow: hidden;
    background: var(--backdrop);
    font-family: "Roboto Condensed", Arial, sans-serif;
  }
  .stage {
    width: 1200px;
    height: 867px;
    display: flex;
    align-items: center;
    justify-content: center;
    gap: 60px;
  }
  .card {
    position: relative;
    width: 520px;
    height: 330px;
    border-radius: 28px;
    border: 3px solid var(--edge-cyan);
    background: var(--card-black);
    overflow: hidden;
  }
  .card--back { background: var(--card-dark); }

  .wordmark {
    color: var(--ink-cyan);
    font-weight: 300;
    text-transform: uppercase;
    letter-spacing: 0.42em;
    text-align: center;
    line-height: 1.5;
  }
  .card--details .wordmark {
    position: absolute;
    left: 44px;
    top: 62px;
    font-size: 22px;
  }
  .wordmark .wordmark-sub { display: block; font-size: 13px; }
  .wordmark-dot {
    display: block;
    width: 44px;
    height: 44px;
    margin: 0 auto 12px;
    border-radius: 50%;
    border: 2px solid currentColor;
  }
  .card--back .wordmark {
    position: absolute;
    inset: 0;
    display: flex;
    flex-direction: column;
    align-items: center;
    justify-content: center;
    color: var(--ink-muted);
    font-size: 24px;
  }

  .person {
    position: absolute;
    left: 262px;
    top: 120px;
    color: var(--ink-cyan);
  }
  .person-name { font-size: 26px; font-weight: 400; }
  .person-role { font-size: 12px; font-weight: 300; margin-top: 2px; }

  .contact-list {
    position: absolute;
    left: 262px;
    top: 200px;
    list-style: none;
    color: var(--ink-cyan);
    font-size: 13px;
    font-weight: 300;
  }
  .contact-list li {
    display: flex;
    align-items: flex-start;
    gap: 10px;
    margin-bottom: 7px;
    line-height: 1.35;
  }
  .contact-icon { width: 13px; height: 13px; flex: none; margin-top: 2px; }
</style>
</head>
<body>
<main class="stage">
  <section class="card card--details">
    <div class="wordmark">
      <span class="wordmark-dot"></span>
      Skyhop
      <span class="wordmark-sub">Rentals</span>
    </div>
    <div class="person">
      <p class="person-name">Marcus Hallworth</p>
      <p class="person-role">Managing Director</p>
    </div>
    <ul class="contact-list">
      <li>
        <svg class="contact-icon" viewBox="0 0 16 16" fill="none" stroke="currentColor" stroke-width="1.4"><circle cx="8" cy="8" r="6.5"/><ellipse cx="8" cy="8" rx="2.8" ry="6.5"/><path d="M1.5 8h13"/></svg>
        www.skyhoprentals.com
      </li>
      <li>
        <svg class="contact-icon" viewBox="0 0 16 16" fill="none" stroke="currentColor" stroke-width="1.4"><rect x="1.5" y="3.5" width="13" height="9" rx="1"/><path d="M1.5 4l6.5 5 6.5-5"/></svg>
        hello@skyhoprentals.net
      </li>
      <li>
        <svg class="contact-icon" viewBox="0 0 16 16" fill="currentColor"><path d="M4 1.5l2.5 3-1.5 1.8c.9 1.9 2.3 3.3 4.2 4.2L11 9l3 2.5-1.3 2.3C7.5 13.6 2.4 8.5 2.2 3.3z"/></svg>
        +1 (555) 014-2290
      </li>
      <li>
        <svg class="contact-icon" viewBox="0 0 16 16" fill="currentColor"><path d="M8 1a5 5 0 0 0-5 5c0 3.8 5 9 5 9s5-5.2 5-9a5 5 0 0 0-5-5zm0 7a2 2 0 1 1 0-4 2 2 0 0 1 0 4z"/></svg>
        <span>Unit 12, 48 Harbor Lane,<br>Brookfield Park, Dr.</span>
      </li>
    </ul>
  </section>

  <section class="card card--back">
    <div class="wordmark">
      <span class="wordmark-dot"></span>
      Skyhop
      <span class="wordmark-sub">Rentals</span>
    </div>
  </section>
</main>
</body>
</html>
```